Kestrel Photography Business Card

I need a business card designed for a photography business based in Perth, Western Australia called Kestrel Photography.

We specialise in wedding, event photography and portrait photography.

The business card must borrow the style of the attached logo.

The hex codes for the colours in the logo are:
#ED1D85 - Pink
#89C23E - Green
#37282F - Black

The name on the card will be:
Name: Toviran
Phone: 0417395268
Website: www.kestrelphotography.com.au
Facebook: kestrelphotography

I am open and happy to accept creative concepts.

I’d like some space at the back for writing notes and appointment details.

```html
<!DOCTYPE html>
<html lang="en">
<head>
<meta charset="utf-8">
<title>Kestrel Photography Business Card</title>
<link rel="stylesheet" href="https://fonts.googleapis.com/css2?family=Didact+Gothic&display=swap">
<style>
  :root {
    --pink: #ED1D85;
    --green: #89C23E;
    --ink: #37282F;
    --paper: #FFFFFF;
    --backdrop: #EDEAE6;
    --text: #2E2529;
    --note-line: rgba(255,255,255,0.38);
  }
  * { box-sizing: border-box; margin: 0; padding: 0; }
  html, body {
    width: 1200px;
    height: 1000px;
    overflow: hidden;
    background: var(--backdrop);
    font-family: "Didact Gothic", "Century Gothic", sans-serif;
    font-weight: 400;
  }
  .stage {
    position: relative;
    width: 1200px;
    height: 1000px;
  }
  .card {
    position: absolute;
    top: 349px;
    width: 540px;
    height: 302px;
    border-radius: 6px;
    box-shadow: 0 6px 18px rgba(0,0,0,0.18);
  }
  .card-front { left: 40px; background: var(--paper); color: var(--text); }
  .card-back { left: 620px; background: var(--ink); color: var(--paper); }

  .brand-mark {
    position: absolute;
    left: 50%;
    transform: translateX(-50%);
    border-radius: 50%;
  }
  .card-front .brand-mark {
    top: 20px;
    width: 74px;
    height: 74px;
    border: 3px solid var(--pink);
  }
  .card-back .brand-mark {
    top: 26px;
    width: 72px;
    height: 72px;
    border: 3px solid var(--paper);
  }

  .wordmark {
    position: absolute;
    left: 0;
    right: 0;
    text-align: center;
    text-transform: uppercase;
    white-space: nowrap;
    font-weight: 400;
  }
  .card-front .wordmark {
    top: 115px;
    font-size: 12.5px;
    letter-spacing: 5.6px;
  }
  .card-back .wordmark {
    top: 114px;
    font-size: 14px;
    letter-spacing: 7px;
  }

  .notes {
    position: absolute;
    left: 50px;
    right: 50px;
    top: 166px;
    list-style: none;
  }
  .notes li {
    height: 30px;
    border-bottom: 1px solid var(--note-line);
  }

  .holder-name {
    position: absolute;
    top: 167px;
    left: 0;
    right: 0;
    text-align: center;
    font-size: 22px;
    font-weight: 400;
    letter-spacing: 2.5px;
    text-transform: uppercase;
  }
  .phone {
    position: absolute;
    top: 200px;
    left: 0;
    right: 0;
    display: flex;
    justify-content: center;
    align-items: center;
    gap: 3px;
    font-size: 14px;
    letter-spacing: 1px;
  }
  .phone svg { width: 15px; height: 15px; }

  .contact-row {
    position: absolute;
    top: 263px;
    display: flex;
    align-items: center;
    gap: 7px;
    font-size: 11px;
    letter-spacing: 1.4px;
    text-transform: uppercase;
    white-space: nowrap;
  }
  .contact-web { left: 22px; }
  .contact-social { left: 330px; }
  .contact-row svg { width: 15px; height: 15px; }
  .social-dot {
    width: 14px;
    height: 14px;
    border-radius: 50%;
    background: var(--text);
  }
</style>
</head>
<body>
<main class="stage">

  <section class="card card-front" aria-label="Business card front">
    <div class="brand-mark" aria-hidden="true"></div>
    <p class="wordmark">Kestrel Photography</p>
    <h1 class="holder-name">Toviran</h1>
    <p class="phone">
      <svg viewBox="0 0 16 16" aria-hidden="true">
        <circle cx="8" cy="8" r="7" fill="none" stroke="#2E2529" stroke-width="1.3"/>
        <path d="M5.4 4.3c.4-.3.8-.2 1 .2l.7 1.2c.2.4.1.7-.2.9l-.4.3c.3.8.9 1.5 1.7 1.9l.3-.4c.2-.3.6-.4.9-.2l1.2.7c.4.2.5.6.2 1l-.5.6c-.4.4-1 .5-1.6.2-1.8-.9-3.1-2.3-3.9-4.1-.2-.6 0-1.2.4-1.6z" fill="#2E2529"/>
      </svg>
      0417395268
    </p>
    <p class="contact-row contact-web">
      <svg viewBox="0 0 16 16" aria-hidden="true">
        <circle cx="8" cy="8" r="7.5" fill="#2E2529"/>
        <g fill="none" stroke="#FFFFFF" stroke-width="0.8">
          <circle cx="8" cy="8" r="5"/>
          <ellipse cx="8" cy="8" rx="2.2" ry="5"/>
          <path d="M3 8h10M4 5.5h8M4 10.5h8"/>
        </g>
      </svg>
      www.kestrelphotography.com.au
    </p>
    <p class="contact-row contact-social">
      <span class="social-dot" aria-hidden="true"></span>
      kestrelphotography
    </p>
  </section>

  <section class="card card-back" aria-label="Business card back">
    <div class="brand-mark" aria-hidden="true"></div>
    <p class="wordmark">Kestrel Photography</p>
    <ul class="notes" aria-label="Space for notes and appointment details">
      <li></li>
      <li></li>
      <li></li>
      <li></li>
    </ul>
  </section>

</main>
</body>
</html>
```